Pelvo BUSINESS CARD

Design an attention-grabbing business cards. Draw inspiration from the provided logo file. Please use the same font style as in the logo.
the back side of the card is for accent/decoration.

Contact Information for Business Card

PLEASE USE PROVIDED BUSINESS CARD SAMPLE

Other font styles liked:
• MIRVALLE

Colors
EB3D1F
EC4F4E
F09395
F8D3D4
FCEDEE

Requirements
Must have
• RED, BLACK COLORS, SOLID BACK COLOR
Nice to have
• MAKE IT FANCY

```html
<!DOCTYPE html>
<html lang="en">
<head>
<meta charset="utf-8">
<title>Pelvo Business Card</title>
<link href="https://fonts.googleapis.com/css2?family=Arimo:wght@400;700&display=swap" rel="stylesheet">
<style>
  :root {
    --backdrop: #e6e6e4;
    --card-white: #ffffff;
    --ink-dark: #2b2b2b;
    --ink-grey: #6a6a6a;
    --rule-grey: #9a9a9a;
    --brand-red: #e0242c;
    --card-black: #232323;
    --tile-dark: #1a1a1a;
    --tile-mid: #4a4a4a;
  }
  * { margin: 0; padding: 0; box-sizing: border-box; }
  html, body { width: 1200px; height: 802px; overflow: hidden; }
  body {
    background: var(--backdrop);
    font-family: "Arimo", Arial, sans-serif;
    position: relative;
  }
  .card {
    position: absolute;
    top: 252px;
    width: 520px;
    height: 297px;
    border-radius: 3px;
    box-shadow: 0 6px 18px rgba(0,0,0,0.18);
    overflow: hidden;
  }
  .card--front { left: 50px; background: var(--card-white); }
  .card--back { left: 630px; background: var(--card-black); }

  /* brand lockup */
  .brand { position: absolute; display: flex; align-items: center; gap: 10px; }
  .brand__mark { width: 40px; height: 40px; background: var(--brand-red); flex: none; }
  .brand__words { display: flex; flex-direction: column; }
  .brand__name { font-weight: 700; font-size: 40px; letter-spacing: 3px; line-height: 1; }
  .brand__tagline { font-size: 8px; letter-spacing: 1.2px; margin-top: 3px; }

  .card--front .brand { left: 190px; top: 34px; }
  .card--front .brand__name,
  .card--front .brand__tagline { color: var(--ink-dark); }

  .front__rule {
    position: absolute; left: 30px; right: 30px; top: 106px;
    height: 1px; background: var(--rule-grey);
  }
  .person { position: absolute; left: 30px; top: 122px; }
  .person__name { color: var(--brand-red); font-weight: 700; font-size: 20px; letter-spacing: 0.5px; line-height: 24px; }
  .person__title { color: var(--ink-grey); font-size: 15px; line-height: 19px; margin-top: 1px; }
  .person__divider { width: 150px; height: 1px; background: var(--rule-grey); margin: 10px 0 8px; }
  .contact { list-style: none; }
  .contact li { display: flex; align-items: center; gap: 8px; color: var(--ink-grey); font-size: 15px; line-height: 22px; }
  .contact svg { width: 12px; height: 12px; flex: none; }
  .address {
    position: absolute; right: 30px; top: 124px;
    text-align: right; color: var(--ink-grey); font-size: 15px; line-height: 21px;
  }

  .back__pattern {
    position: absolute; inset: 0;
    background:
      radial-gradient(ellipse at 85% 30%, rgba(120,120,120,0.55), transparent 60%),
      linear-gradient(135deg, var(--tile-dark) 0%, var(--card-black) 45%, var(--tile-mid) 100%);
  }
  .card--back .brand { left: 240px; top: 150px; }
  .card--back .brand__mark { width: 58px; height: 58px; background: var(--card-white); }
  .card--back .brand__name { color: var(--card-white); font-size: 44px; }
  .card--back .brand__tagline { color: var(--card-white); }
</style>
</head>
<body>

  <section class="card card--front" aria-label="Front of business card">
    <div class="brand">
      <span class="brand__mark"></span>
      <div class="brand__words">
        <span class="brand__name">PELVO</span>
        <span class="brand__tagline">LOGISTICS DONE RIGHT</span>
      </div>
    </div>
    <div class="front__rule"></div>

    <div class="person">
      <div class="person__name">TOMAS REYNA</div>
      <div class="person__title">President</div>
      <div class="person__divider"></div>
      <ul class="contact">
        <li>
          <svg viewBox="0 0 12 12"><path fill="var(--brand-red)" d="M2.5 1l2 2.2-1 1.3a6 6 0 0 0 4 4l1.3-1 2.2 2-1.3 1.5C5.5 11 1 6.5 1 2.3z"/></svg>
          555-014-2276
        </li>
        <li>
          <svg viewBox="0 0 12 12"><rect x="3" y="0.8" width="6" height="10.4" rx="1" fill="none" stroke="var(--brand-red)" stroke-width="1.3"/><circle cx="6" cy="9.4" r="0.7" fill="var(--brand-red)"/></svg>
          555-018-3390
        </li>
        <li>
          <svg viewBox="0 0 12 12"><rect x="0.5" y="2.5" width="11" height="7.5" fill="var(--brand-red)"/><path d="M0.8 2.8L6 6.8l5.2-4" fill="none" stroke="#fff" stroke-width="1"/></svg>
          TReyna@pelvo-llc.com
        </li>
        <li>
          <svg viewBox="0 0 12 12"><circle cx="6" cy="6" r="5.5" fill="var(--brand-red)"/><path d="M0.8 6h10.4M6 0.8c-2.6 3-2.6 7.4 0 10.4M6 0.8c2.6 3 2.6 7.4 0 10.4" fill="none" stroke="#fff" stroke-width="0.8"/></svg>
          www.Pelvo-LLC.com
        </li>
      </ul>
    </div>

    <div class="address">
      1840 N. 250 West<br>
      Halden, IN, 40512
    </div>
  </section>

  <section class="card card--back" aria-label="Back of business card">
    <div class="back__pattern" role="img" aria-label="Embossed grid of repeated square tiles in black and grey"></div>
    <div class="brand">
      <span class="brand__mark"></span>
      <div class="brand__words">
        <span class="brand__name">PELVO</span>
        <span class="brand__tagline">LOGISTICS DONE RIGHT</span>
      </div>
    </div>
  </section>

</body>
</html>
```